Maple Crest Venture Fund

Take current power point presentation and make it uniform in color and font, and create designs that pop throughout the presentation. Right now, it is dull and mundane.

```html
<!DOCTYPE html>
<html lang="en">
<head>
<meta charset="utf-8">
<title>Maple Crest Venture Fund – Presentation</title>
<link href="https://fonts.googleapis.com/css2?family=Montserrat:wght@400;600;700&family=Poppins:wght@400;600&display=swap" rel="stylesheet">
<style>
:root{
  --blue:#1462b8;
  --blue-dark:#0d4a8f;
  --ink:#1d1d1f;
  --text:#3a3a3c;
  --muted:#6b6b70;
  --card:#ffffff;
  --page:#ffffff;
  --line:#c9d6e6;
}
*{box-sizing:border-box;margin:0;padding:0}
html,body{width:1200px;height:349px;overflow:hidden;background:var(--page)}
body{position:relative;font-family:'Poppins',sans-serif;color:var(--text)}
.slide{position:absolute;width:293px;height:165px;background:#fff;box-shadow:0 0 3px rgba(0,0,0,.18);overflow:hidden}
.s1{left:6px;top:7px}.s2{left:306px;top:7px}.s3{left:607px;top:7px}.s4{left:906px;top:7px}
.s5{left:6px;top:178px}.s6{left:306px;top:178px}.s7{left:607px;top:178px}.s8{left:906px;top:178px}
.abs{position:absolute}
.title-bar{position:absolute;left:0;top:8px;width:5px;height:19px;background:var(--blue)}
.slide-title{position:absolute;left:13px;top:11px;font:700 9.2px 'Montserrat',sans-serif;color:var(--ink);letter-spacing:.2px;white-space:nowrap}
.brand{position:absolute;right:8px;top:9px;font:700 12px 'Montserrat',sans-serif;color:var(--blue);letter-spacing:.3px}
.corner{position:absolute;right:0;bottom:0;width:18px;height:18px}
.centered{position:absolute;left:0;width:100%;text-align:center}
.sub-head{font:600 4.6px 'Montserrat',sans-serif;color:var(--blue)}
.lead{font-size:3.5px;line-height:5.6px;color:var(--text)}
.card{position:absolute;background:var(--card);box-shadow:0 0 2.5px rgba(0,0,0,.16)}
.card-title{font:600 4.1px 'Montserrat',sans-serif;color:var(--ink);text-align:center}
.card-text{font-size:3.2px;line-height:5.3px;color:var(--muted);text-align:center}

/* cover */
.s1 .cover-bg{position:absolute;inset:0;background:radial-gradient(circle at 70% 40%,#e9eff6 0%,#f4f7fb 55%,#eef2f7 100%)}
.s1 .cover-brand{position:absolute;left:72px;top:44px;font:700 56px 'Montserrat',sans-serif;color:var(--blue);letter-spacing:2px}
.s1 .cover-name{position:absolute;left:86px;top:104px;font:400 7.1px 'Montserrat',sans-serif;color:#3b4a5c;letter-spacing:1px}

/* disclosure */
.s2 .legal{position:absolute;left:13px;top:32px;width:268px;font-size:3.4px;line-height:6px;color:var(--text)}
.s2 .legal p{margin-bottom:6px}

/* agenda */
.s3 .agenda-photo{position:absolute;left:0;top:0;width:108px;height:165px;background:linear-gradient(160deg,#56606b 0%,#3c4a52 50%,#2f4a45 100%)}
.s3 .agenda-word{position:absolute;left:54px;top:82px;transform:translate(-50%,-50%) rotate(-90deg);font:700 9.5px 'Montserrat',sans-serif;color:#fff;letter-spacing:1px}
.agenda-item{position:absolute;left:134px;font:600 5.1px 'Montserrat',sans-serif;color:var(--ink)}
.agenda-rule{position:absolute;left:108px;width:103px;height:.5px;background:var(--line)}
.agenda-icon{position:absolute;left:108px;width:22px;height:12px}
.agenda-sub{position:absolute;left:134px;font-size:3.2px;color:var(--text);white-space:nowrap}
.agenda-sub::before{content:"";display:inline-block;width:2.4px;height:2.4px;border-radius:50%;background:var(--blue);margin-right:3px;vertical-align:middle}

/* strategy */
.num{position:absolute;left:50%;transform:translateX(-50%);width:17px;height:17px;border-radius:50%;background:var(--blue);color:#fff;font:600 8px 'Montserrat',sans-serif;text-align:center;line-height:17px}

/* management */
.portrait{position:absolute;width:20px;height:20px;border-radius:50%;background:linear-gradient(135deg,#8c8f94,#4a4d52)}
.person{position:absolute;font:600 4.2px 'Montserrat',sans-serif;color:var(--blue)}
.bio{position:absolute;font-size:2.9px;line-height:5.3px;color:var(--text)}

/* icons */
.icon-ring{position:absolute;width:24px;height:24px}

/* advantages */
.adv-label{position:absolute;font:600 5px 'Montserrat',sans-serif;color:var(--ink);text-align:center;line-height:7.5px}
.adv-text{position:absolute;font-size:3.8px;line-height:6.5px;color:var(--muted);text-align:center}

/* diligence */
.photo{position:absolute;top:62px;width:83px;height:47px}
</style>
</head>
<body>

<!-- Cover -->
<section class="slide s1">
  <div class="cover-bg" role="img" aria-label="Soft network and finance backdrop"></div>
  <div class="cover-brand">MCVF</div>
  <div class="cover-name">Maple Crest Venture Fund</div>
</section>

<!-- Disclosure -->
<section class="slide s2">
  <div class="title-bar"></div>
  <h1 class="slide-title">DISCLOSURE</h1>
  <div class="brand">MCVF</div>
  <div class="legal">
    <p>This Presentation is a summary and does not constitute an offer to sell, or a solicitation of any offer to buy or sell, any securities. Any such offer will be made solely to qualified investors by means of an offering memorandum and related subscription materials, which will contain material information not contained herein. This Presentation is not intended to replace any such offering memorandum.</p>
    <p>No assurance can be given that the objectives discussed herein will be achieved and results may vary substantially on a quarterly, annual or other periodic basis. Past performance is not necessarily indicative of future results.</p>
    <p>Prospective reviewers should not construe this Presentation, any offering memorandum or any other communication received from MCVF or its affiliates as legal, accounting, tax, investment or other advice, and each reviewer should consult with its own counsel and advisors as to all legal, tax, regulatory, financial and related matters.</p>
    <p>In addition, certain information contained herein has been provided by third parties and has not been independently verified by MCVF. MCVF makes no representation or warranty, express or implied, as to the accuracy or the completeness of such information, and accepts no liability for any direct or consequential losses arising from the use of such information.</p>
    <p>This Presentation is confidential and proprietary to MCVF. Accordingly, this Presentation is to be treated as strictly confidential and not disclosed, directly or indirectly, to any party other than the person to whom it has been delivered and such person's professional advisors. Any distribution of this Presentation, in whole or in part, or the divulgence of any of its contents, is unauthorized. No person has been authorized to give any information or make any representations other than as set forth herein.</p>
  </div>
  <svg class="corner" viewBox="0 0 18 18"><polygon points="18,0 18,18 0,18" fill="#1462b8"/><line x1="16" y1="1" x2="1" y2="16" stroke="#fff" stroke-width=".5"/><text x="13" y="16" font-size="3" fill="#fff" font-family="Poppins">02</text></svg>
</section>

<!-- Agenda -->
<section class="slide s3">
  <div class="agenda-photo" role="img" aria-label="Dark financial chart backdrop"></div>
  <div class="agenda-word">AGENDA</div>
  <div class="brand">MCVF</div>
  <svg class="agenda-icon" style="top:6px" viewBox="0 0 22 12"><rect x="0" y="1" width="22" height="10" fill="#1462b8"/><circle cx="16" cy="6" r="4" fill="none" stroke="#fff" stroke-width=".7"/><polyline points="15,4 17,6 15,8" fill="none" stroke="#fff" stroke-width=".7"/></svg>
  <div class="agenda-item" style="top:9px">Objectives</div>
  <div class="agenda-rule" style="top:20px"></div>
  <svg class="agenda-icon" style="top:24px" viewBox="0 0 22 12"><rect x="0" y="1" width="22" height="10" fill="#1462b8"/><circle cx="16" cy="6" r="4" fill="none" stroke="#fff" stroke-width=".7"/><polyline points="15,4 17,6 15,8" fill="none" stroke="#fff" stroke-width=".7"/></svg>
  <div class="agenda-item" style="top:27px">Strategy</div>
  <div class="agenda-rule" style="top:37px"></div>
  <svg class="agenda-icon" style="top:40px" viewBox="0 0 22 12"><rect x="0" y="1" width="22" height="10" fill="#1462b8"/><circle cx="16" cy="6" r="4" fill="none" stroke="#fff" stroke-width=".7"/><polyline points="15,4 17,6 15,8" fill="none" stroke="#fff" stroke-width=".7"/></svg>
  <div class="agenda-item" style="top:41px">The MCVF organization</div>
  <div class="agenda-sub" style="top:49px">Senior Management</div>
  <div class="agenda-sub" style="top:55px">MCVF's competitive advantage</div>
  <div class="agenda-sub" style="top:61px">How we are different</div>
  <div class="agenda-rule" style="top:71px"></div>
  <svg class="agenda-icon" style="top:76px" viewBox="0 0 22 12"><rect x="0" y="1" width="22" height="10" fill="#1462b8"/><circle cx="16" cy="6" r="4" fill="none" stroke="#fff" stroke-width=".7"/><polyline points="15,4 17,6 15,8" fill="none" stroke="#fff" stroke-width=".7"/></svg>
  <div class="agenda-item" style="top:78px">Performance</div>
  <div class="agenda-rule" style="top:88px"></div>
  <svg class="agenda-icon" style="top:92px" viewBox="0 0 22 12"><rect x="0" y="1" width="22" height="10" fill="#1462b8"/><circle cx="16" cy="6" r="4" fill="none" stroke="#fff" stroke-width=".7"/><polyline points="15,4 17,6 15,8" fill="none" stroke="#fff" stroke-width=".7"/></svg>
  <div class="agenda-item" style="top:95px">Structure &amp; Terms</div>
  <div class="agenda-rule" style="top:105px"></div>
  <svg class="agenda-icon" style="top:111px" viewBox="0 0 22 12"><rect x="0" y="1" width="22" height="10" fill="#1462b8"/><circle cx="16" cy="6" r="4" fill="none" stroke="#fff" stroke-width=".7"/><polyline points="15,4 17,6 15,8" fill="none" stroke="#fff" stroke-width=".7"/></svg>
  <div class="agenda-item" style="top:112px">The MCVF organization</div>
  <div class="agenda-sub" style="top:120px">Why MCVF Direct Invest Strategy?</div>
  <div class="agenda-sub" style="top:126px">Industry Overview</div>
  <div class="agenda-sub" style="top:132px">Differentiation Between PIPEs and Direct</div>
  <div class="agenda-sub" style="top:138px">Investments</div>
  <div class="agenda-sub" style="top:144px">Capital/Deal Structure</div>
  <div class="agenda-sub" style="top:150px">Process</div>
  <div class="agenda-sub" style="top:156px">Protection/Risk</div>
  <svg class="corner" viewBox="0 0 18 18"><polygon points="18,0 18,18 0,18" fill="#1462b8"/><line x1="16" y1="1" x2="1" y2="16" stroke="#fff" stroke-width=".5"/><text x="13" y="16" font-size="3" fill="#fff" font-family="Poppins">03</text></svg>
</section>

<!-- Investment strategy -->
<section class="slide s4">
  <div class="title-bar"></div>
  <h1 class="slide-title">INVESTMENT STRATEGY</h1>
  <div class="brand">MCVF</div>
  <div class="centered sub-head" style="top:33px">MCVF Funding Specialization</div>
  <div class="centered lead" style="top:42px;left:40px;width:213px">MCVF focuses on financing Development Stage, Emerging Growth, and Distressed public companies. This is achieved through a structured approach, wherein investments are tranched over a one- to four-year timeframe.</div>
  <div class="centered sub-head" style="top:69px">Objectives</div>
  <div class="centered lead" style="top:78px">Our strategy serves three key purposes</div>
  <div class="card" style="left:26px;top:87px;width:77px;height:61px">
    <div class="num" style="top:6px">1</div>
    <div class="card-title abs" style="top:28px;width:100%">Minimize Dilution</div>
    <div class="card-text abs" style="top:37px;left:8px;width:61px">Limits the dilution of the issuer's common stock</div>
  </div>
  <div class="card" style="left:107px;top:87px;width:78px;height:61px">
    <div class="num" style="top:6px">2</div>
    <div class="card-title abs" style="top:28px;width:100%">Mitigate Risk</div>
    <div class="card-text abs" style="top:37px;left:6px;width:66px">Reduces exposure by allowing cessation of further investment in the event of a material adverse change.</div>
  </div>
  <div class="card" style="left:189px;top:87px;width:77px;height:61px">
    <div class="num" style="top:6px">3</div>
    <div class="card-title abs" style="top:28px;width:100%">Protect Capital</div>
    <div class="card-text abs" style="top:37px;left:8px;width:61px">Safeguards against losses stemming from fraud or corporate malfeasance.</div>
  </div>
  <svg class="corner" viewBox="0 0 18 18"><polygon points="18,0 18,18 0,18" fill="#1462b8"/><line x1="16" y1="1" x2="1" y2="16" stroke="#fff" stroke-width=".5"/><text x="13" y="16" font-size="3" fill="#fff" font-family="Poppins">04</text></svg>
</section>

<!-- Senior management -->
<section class="slide s5">
  <div class="title-bar" style="top:9px"></div>
  <h1 class="slide-title" style="top:13px">SENIOR MANAGEMENT</h1>
  <div class="brand">MCVF</div>
  <div class="card" style="left:11px;top:31px;width:273px;height:60px">
    <div class="portrait" style="left:4px;top:4px" role="img" aria-label="Portrait of Daniel Whitcombe"></div>
    <div class="person" style="left:27px;top:5px">Daniel Whitcombe</div>
    <div class="bio" style="left:27px;top:11px;width:242px">Daniel Whitcombe is a business executive with extensive C-level and board leadership experience across private and public companies. He is a Founder and Member of MCVF Investments LLC and previously founded a cell storage company, serving as its Chairman and CEO.</div>
    <div class="bio" style="left:4px;top:27px;width:265px">Before joining MCVF, he worked as a licensed investment banker providing microcap advisory and capital introduction services to publicly traded companies. He has advised venture capital funds, family offices and other institutional investors, and previously held leadership positions on several biotech committees. He holds a Bachelor of Arts in Biology.</div>
  </div>
  <div class="card" style="left:11px;top:94px;width:134px;height:66px">
    <div class="portrait" style="left:4px;top:3px" role="img" aria-label="Portrait of Evan Loring"></div>
    <div class="person" style="left:27px;top:4px">Evan Loring</div>
    <div class="bio" style="left:27px;top:10px;width:104px">Evan Loring is a Founder and Member of MCVF Investments LLC, bringing over 17 years of experience in PIPE transactions.</div>
    <div class="bio" style="left:4px;top:26px;width:127px">Prior to launching his own funds, he co-founded multiple investment funds and managed portfolios for a family of funds, overseeing companies with a focus on private equity financing. He holds a Bachelor of Arts in Finance.</div>
  </div>
  <div class="card" style="left:149px;top:94px;width:134px;height:66px">
    <div class="portrait" style="left:4px;top:3px" role="img" aria-label="Portrait of Rahim Castell"></div>
    <div class="person" style="left:27px;top:4px">Rahim Castell</div>
    <div class="bio" style="left:27px;top:10px;width:104px">Rahim Castell is a Founder and Member of MCVF Investments LLC with extensive experience investing in public companies since 2011.</div>
    <div class="bio" style="left:4px;top:26px;width:127px">His professional background spans roles at a state agency and an IT company prior to his move into finance. He earned his Juris Doctor and holds a Bachelor's degree in Philosophy, Politics and Law.</div>
  </div>
  <svg class="corner" viewBox="0 0 18 18"><polygon points="18,0 18,18 0,18" fill="#1462b8"/><line x1="16" y1="1" x2="1" y2="16" stroke="#fff" stroke-width=".5"/><text x="13" y="16" font-size="3" fill="#fff" font-family="Poppins">05</text></svg>
</section>

<!-- How we are different -->
<section class="slide s6">
  <div class="title-bar"></div>
  <h1 class="slide-title" style="top:12px">HOW WE ARE DIFFERENT</h1>
  <div class="brand">MCVF</div>
  <div class="centered sub-head" style="top:34px">Investment Structures</div>
  <div class="centered lead" style="top:44px;left:45px;width:203px">MCVF has conducted research on existing investment frameworks and continually adapts its approach to provide companies with tailored investments while minimizing transaction costs and fees.</div>
  <div class="card" style="left:10px;top:62px;width:65px;height:85px">
    <svg class="icon-ring" style="left:20px;top:7px" viewBox="0 0 24 24"><circle cx="12" cy="12" r="11.5" fill="none" stroke="#1462b8" stroke-width=".5" stroke-dasharray="1 1"/><circle cx="12" cy="12" r="10" fill="#1462b8"/><rect x="8" y="7" width="6" height="9" fill="none" stroke="#fff" stroke-width=".7"/><line x1="9.5" y1="10" x2="12.5" y2="10" stroke="#fff" stroke-width=".6"/><line x1="9.5" y1="12" x2="12.5" y2="12" stroke="#fff" stroke-width=".6"/><circle cx="15" cy="15" r="2.2" fill="none" stroke="#fff" stroke-width=".7"/></svg>
    <div class="card-title abs" style="top:38px;width:100%">Capital Efficiency</div>
    <div class="card-text abs" style="top:45px;left:4px;width:57px">MCVF's investment strategy enables companies to retain a greater portion of the capital raised while delivering substantial returns to investors.</div>
  </div>
  <div class="card" style="left:79px;top:62px;width:65px;height:85px">
    <svg class="icon-ring" style="left:20px;top:7px" viewBox="0 0 24 24"><circle cx="12" cy="12" r="11.5" fill="none" stroke="#1462b8" stroke-width=".5" stroke-dasharray="1 1"/><circle cx="12" cy="12" r="10" fill="#1462b8"/><rect x="7" y="8" width="10" height="7" fill="none" stroke="#fff" stroke-width=".7"/><polyline points="8.5,13.5 11,11 13,12.5 15.5,9.5" fill="none" stroke="#fff" stroke-width=".7"/><line x1="12" y1="15" x2="12" y2="17" stroke="#fff" stroke-width=".7"/></svg>
    <div class="card-title abs" style="top:39px;width:100%">Long-Term Focus</div>
    <div class="card-text abs" style="top:46px;left:4px;width:57px">By adopting a long-term perspective on both entry and exit strategies, MCVF minimizes market disruption.</div>
  </div>
  <div class="card" style="left:149px;top:62px;width:65px;height:85px">
    <svg class="icon-ring" style="left:20px;top:7px" viewBox="0 0 24 24"><circle cx="12" cy="12" r="11.5" fill="none" stroke="#1462b8" stroke-width=".5" stroke-dasharray="1 1"/><circle cx="12" cy="12" r="10" fill="#1462b8"/><circle cx="12" cy="10" r="3" fill="none" stroke="#fff" stroke-width=".7"/><path d="M6.5 15 Q9 13.5 12 15.5 Q15 17 17.5 14.5" fill="none" stroke="#fff" stroke-width=".7"/></svg>
    <div class="card-title abs" style="top:38px;width:100%;line-height:6.5px">Flexible Prepayment<br>Options</div>
    <div class="card-text abs" style="top:51px;left:4px;width:57px">MCVF incorporates prepayment provisions, allowing companies to repay investments within 6 months at a predetermined amount.</div>
  </div>
  <div class="card" style="left:218px;top:62px;width:65px;height:85px">
    <svg class="icon-ring" style="left:20px;top:7px" viewBox="0 0 24 24"><circle cx="12" cy="12" r="11.5" fill="none" stroke="#1462b8" stroke-width=".5" stroke-dasharray="1 1"/><circle cx="12" cy="12" r="10" fill="#1462b8"/><circle cx="12" cy="12" r="5" fill="none" stroke="#fff" stroke-width=".7"/><line x1="12" y1="12" x2="14.5" y2="9.5" stroke="#fff" stroke-width=".7"/></svg>
    <div class="card-title abs" style="top:38px;width:100%">Optimized Returns</div>
    <div class="card-text abs" style="top:45px;left:4px;width:57px">Through the deployment of multiple investment structures, MCVF reduces liabilities, funds asset growth, ensures timely exits, and maximizes upside potential.</div>
  </div>
  <svg class="corner" viewBox="0 0 18 18"><polygon points="18,0 18,18 0,18" fill="#1462b8"/><line x1="16" y1="1" x2="1" y2="16" stroke="#fff" stroke-width=".5"/><text x="13" y="16" font-size="3" fill="#fff" font-family="Poppins">06</text></svg>
</section>

<!-- Why direct investment -->
<section class="slide s7">
  <div class="title-bar"></div>
  <h1 class="slide-title" style="top:12px">WHY MCVF'S DIRECT INVESTMENT STRATEGY?</h1>
  <div class="brand">MCVF</div>
  <svg class="abs" style="left:0;top:0" width="293" height="165" viewBox="0 0 293 165">
    <path d="M53 169 A93 93 0 0 1 239 169" fill="none" stroke="#1462b8" stroke-width=".6" stroke-dasharray="2 1.5"/>
    <path d="M73 169 A73 73 0 0 1 219 169" fill="none" stroke="#1d1d1f" stroke-width=".6"/>
    <g fill="#1462b8" stroke="#fff" stroke-width="1.2">
      <circle cx="146" cy="76" r="12.5"/><circle cx="87" cy="99" r="12.5"/><circle cx="60" cy="143" r="12.5"/><circle cx="204" cy="98" r="12.5"/><circle cx="228" cy="142" r="12.5"/>
    </g>
    <g fill="none" stroke="#1462b8" stroke-width=".4">
      <circle cx="146" cy="76" r="13.7"/><circle cx="87" cy="99" r="13.7"/><circle cx="60" cy="143" r="13.7"/><circle cx="204" cy="98" r="13.7"/><circle cx="228" cy="142" r="13.7"/>
    </g>
    <g fill="none" stroke="#fff" stroke-width=".8">
      <rect x="140" y="73" width="3" height="7"/><rect x="144.5" y="70" width="3" height="10"/><rect x="149" y="72" width="3" height="8"/>
      <polygon points="87,92 94,105 80,105"/><line x1="87" y1="96" x2="87" y2="101"/>
      <line x1="55" y1="148" x2="65" y2="138"/><polyline points="60,138 65,138 65,143"/>
      <circle cx="204" cy="98" r="6"/><line x1="198" y1="98" x2="210" y2="98"/><ellipse cx="204" cy="98" rx="2.6" ry="6"/>
      <polyline points="223,142 227,146 234,138"/>
    </g>
  </svg>
  <div class="adv-label" style="left:116px;top:29px;width:60px">Equity Kickers</div>
  <div class="adv-text" style="left:116px;top:37px;width:60px">Warrants or stock provide additional upside potential.</div>
  <div class="adv-label" style="left:16px;top:83px;width:60px">Risk Management</div>
  <div class="adv-text" style="left:10px;top:92px;width:72px">Achieved through tranching strategies.</div>
  <div class="adv-label" style="left:0;top:124px;width:56px">Upside Potential</div>
  <div class="adv-text" style="left:3px;top:133px;width:50px">through strategic investments</div>
  <div class="adv-label" style="left:221px;top:77px;width:50px">Market Arbitrage/ Appreciation</div>
  <div class="adv-text" style="left:220px;top:95px;width:52px">Participation at a fixed discount at funding allowing arbitrage at...</div>
  <div class="adv-label" style="left:240px;top:122px;width:50px">Robust Deal</div>
  <div class="adv-text" style="left:240px;top:131px;width:52px">Access to a vast pipeline of deals within various sectors.</div>
  <div class="abs" style="left:116px;top:126px;width:60px;text-align:center;font:700 13px 'Montserrat',sans-serif;color:var(--blue)">MCVF</div>
  <div class="abs" style="left:106px;top:149px;width:80px;text-align:center;font:600 5.3px 'Montserrat',sans-serif;color:var(--blue)">Key Advantages</div>
  <svg class="corner" viewBox="0 0 18 18"><polygon points="18,0 18,18 0,18" fill="#1462b8"/><line x1="16" y1="1" x2="1" y2="16" stroke="#fff" stroke-width=".5"/><text x="13" y="16" font-size="3" fill="#fff" font-family="Poppins">07</text></svg>
</section>

<!-- Process -->
<section class="slide s8">
  <div class="title-bar"></div>
  <h1 class="slide-title" style="top:11px">PROCESS – ON GOING DUE DILIGENCE</h1>
  <div class="brand">MCVF</div>
  <div class="centered sub-head" style="top:30px">Ongoing Due Diligence and Monitoring</div>
  <div class="centered lead" style="top:39px;left:40px;width:213px">Once an investment is made, the due diligence is typically performed on an ongoing and regular basis. This ongoing process involves analysis and evaluation of all relevant financial, legal, and accounting information, both historical and current.</div>
  <div class="card" style="left:13px;top:62px;width:83px;height:92px"></div>
  <div class="card" style="left:104px;top:62px;width:83px;height:92px"></div>
  <div class="card" style="left:196px;top:62px;width:83px;height:92px"></div>
  <div class="photo" style="left:13px;background:linear-gradient(135deg,#d9e3ee,#2c5e9e 60%,#1b3457)" role="img" aria-label="Team reviewing financial reports at a desk"></div>
  <div class="photo" style="left:104px;background:linear-gradient(135deg,#0f2c48,#2d6c9c 55%,#bfd3e3)" role="img" aria-label="Investor analysing market charts on screens"></div>
  <div class="photo" style="left:196px;background:linear-gradient(135deg,#8aa6c4,#3e73b0 55%,#e7a73a)" role="img" aria-label="Laptop showing portfolio charts"></div>
  <svg class="abs" style="left:0;top:99px" width="293" height="18" viewBox="0 0 293 18">
    <g fill="#1462b8" stroke="#fff" stroke-width="1"><circle cx="54.5" cy="9" r="7.5"/><circle cx="145.5" cy="9" r="7.5"/><circle cx="237.5" cy="9" r="7.5"/></g>
    <g fill="none" stroke="#fff" stroke-width=".6">
      <rect x="51" y="6" width="7" height="6"/><line x1="52.5" y1="9" x2="56.5" y2="9"/>
      <circle cx="145.5" cy="9" r="3.5"/><line x1="145.5" y1="5.5" x2="145.5" y2="12.5"/>
      <polyline points="234.5,9 236.7,11.2 240.5,7"/>
    </g>
  </svg>
  <div class="card-title abs" style="left:13px;top:118px;width:83px">Monthly Reviews</div>
  <div class="card-text abs" style="left:16px;top:125px;width:77px">The team conducts monthly due diligence on portfolio companies to ensure continued oversight.</div>
  <div class="card-title abs" style="left:104px;top:118px;width:83px">Tranching Integration</div>
  <div class="card-text abs" style="left:107px;top:125px;width:77px">This ongoing due diligence is closely aligned with the tranching strategy, providing a continuous framework for monitoring portfolio companies.</div>
  <div class="card-title abs" style="left:196px;top:118px;width:83px">Problem Resolution</div>
  <div class="card-text abs" style="left:199px;top:125px;width:77px">If issues arise, the team can become more involved to safeguard investors' rights and protect capital investments.</div>
  <svg class="corner" viewBox="0 0 18 18"><polygon points="18,0 18,18 0,18" fill="#1462b8"/><line x1="16" y1="1" x2="1" y2="16" stroke="#fff" stroke-width=".5"/><text x="13" y="16" font-size="3" fill="#fff" font-family="Poppins">08</text></svg>
</section>

</body>
</html>
```